Business Card Design

new real estate company in the Colorado mountains would like fun..creative.. pines trees and house and dog(s)? heart? I love colors

I am also asking for a logo design then to biz cards..

Industry/Entity Type

Real Estate

Contact Information for Business Card

Meadowlark Bend Realty

Rosalind Tavers
"Your Trail Guide to Home Sweet Home!"
555-316-0847
rosalindmtavers@brightpost.example

```html
<!DOCTYPE html>
<html lang="en">
<head>
<meta charset="utf-8">
<title>Meadowlark Bend Realty – Business Card</title>
<link href="https://fonts.googleapis.com/css2?family=Marcellus&family=Open+Sans:wght@400;600;700&display=swap" rel="stylesheet">
<style>
  :root {
    --page-bg: #e8e5e0;
    --card-deep: #2a2590;
    --card-mid: #3d34a6;
    --card-glow: #6b62bd;
    --brand-cyan: #3ec3e6;
    --accent-orange: #ef7a35;
    --text-white: #ffffff;
    --tree-shade: #241f7d;
  }
  html, body {
    margin: 0;
    padding: 0;
    width: 1200px;
    height: 1023px;
    overflow: hidden;
    background: var(--page-bg);
  }
  .canvas {
    position: relative;
    width: 1200px;
    height: 1023px;
  }
  .business-card {
    position: absolute;
    left: 100px;
    top: 226px;
    width: 1000px;
    height: 571px;
    border-radius: 6px;
    overflow: hidden;
    background: radial-gradient(ellipse 60% 70% at 42% 52%, var(--card-glow) 0%, var(--card-mid) 50%, var(--card-deep) 100%);
    box-shadow: 0 18px 40px rgba(0,0,0,0.25);
  }
  .tree-line {
    position: absolute;
    left: 0;
    top: 0;
    width: 1000px;
    height: 120px;
    background: linear-gradient(180deg, rgba(36,31,125,0.6) 0%, rgba(36,31,125,0) 100%);
    -webkit-mask-image: linear-gradient(90deg, transparent 0%, transparent 40%, #000 70%);
    mask-image: linear-gradient(90deg, transparent 0%, transparent 40%, #000 70%);
  }
  .brand {
    position: absolute;
    left: 60px;
    top: 150px;
    display: flex;
    align-items: center;
    gap: 28px;
  }
  .brand-square {
    width: 86px;
    height: 86px;
    background: var(--brand-cyan);
    flex: none;
  }
  .brand-name {
    margin: 0;
    font-weight: 400;
    text-transform: uppercase;
    line-height: 1;
  }
  .brand-name .line-lead {
    display: block;
    font-family: "Marcellus", serif;
    font-size: 66px;
    letter-spacing: 2px;
    color: var(--brand-cyan);
  }
  .brand-name .line-tail {
    display: block;
    font-family: "Open Sans", sans-serif;
    font-size: 34px;
    letter-spacing: 1px;
    margin-top: 8px;
    color: var(--accent-orange);
  }
  .agent-name {
    position: absolute;
    left: 174px;
    top: 352px;
    margin: 0;
    font-family: "Open Sans", sans-serif;
    font-weight: 700;
    font-size: 28px;
    letter-spacing: 1px;
    color: var(--brand-cyan);
    text-transform: uppercase;
  }
  .contact-list {
    position: absolute;
    left: 520px;
    top: 300px;
    margin: 0;
    padding: 0;
    list-style: none;
    font-family: "Open Sans", sans-serif;
    font-size: 21px;
    color: var(--text-white);
  }
  .contact-list li {
    display: flex;
    align-items: center;
    gap: 12px;
    margin-bottom: 10px;
  }
  .contact-icon {
    width: 20px;
    height: 20px;
    flex: none;
  }
  .tagline-band {
    position: absolute;
    left: 0;
    top: 0;
    width: 1000px;
    height: 571px;
  }
  .tagline-text {
    font-family: "Open Sans", sans-serif;
    font-weight: 700;
    font-size: 21px;
    letter-spacing: 1px;
    fill: var(--text-white);
  }
</style>
</head>
<body>
<div class="canvas">
  <div class="business-card">
    <div class="tree-line" role="img" aria-label="Faint row of pine tree silhouettes along the top edge"></div>

    <div class="brand">
      <div class="brand-square"></div>
      <h1 class="brand-name"><span class="line-lead">Meadowlark</span><span class="line-tail">Bend Realty</span></h1>
    </div>

    <p class="agent-name">Rosalind Tavers</p>

    <ul class="contact-list">
      <li>
        <svg class="contact-icon" viewBox="0 0 20 20" aria-hidden="true">
          <rect width="20" height="20" rx="3" fill="var(--accent-orange)"/>
          <path d="M6 4.5l2 .3.8 3-1.3 1a7 7 0 0 0 3.7 3.7l1-1.3 3 .8.3 2c-.2 1-1 1.5-2 1.5A10 10 0 0 1 4.5 6.5c0-1 .5-1.8 1.5-2z" fill="var(--text-white)"/>
        </svg>
        <span>555-316-0847</span>
      </li>
      <li>
        <svg class="contact-icon" viewBox="0 0 20 20" aria-hidden="true">
          <rect width="20" height="20" rx="3" fill="var(--accent-orange)"/>
          <rect x="4" y="6" width="12" height="8" fill="none" stroke="var(--text-white)" stroke-width="1.5"/>
          <path d="M4 6l6 5 6-5" fill="none" stroke="var(--text-white)" stroke-width="1.5"/>
        </svg>
        <span>rosalindmtavers@brightpost.example</span>
      </li>
    </ul>

    <svg class="tagline-band" viewBox="0 0 1000 571">
      <defs>
        <path id="tagline-path" d="M430 558 Q700 494 990 462"/>
      </defs>
      <path d="M270 571 Q640 458 1000 404" fill="none" stroke="var(--accent-orange)" stroke-width="7"/>
      <path d="M300 571 Q650 472 1000 420 L1000 571 Z" fill="var(--brand-cyan)"/>
      <text class="tagline-text"><textPath href="#tagline-path">YOUR TRAIL GUIDE TO HOME SWEET HOME!</textPath></text>
    </svg>
  </div>
</div>
</body>
</html>
```